グローバルナビ
左サイドメニュー
横幅:960px

今回は、コンペ用のデザイン作成依頼となります。ロゴや電話番号・その他画像データ等サンプルで作成頂ければ幸いです。

《クライアント様からの要望》
すっきりとした見やすいホームページで、患者様やご家族の方に優しい・温かいイメージをもって欲しい。
ロゴに使用されているカラーコードは、「24569d」となります。基調色として取り入れてください。

総合病院で診療科目が多い為、利用者が情報を探しやすいように工夫してください。
病院のPRポイントとしては、「救急患者の受入れを断らない」地域に最先端医療で貢献する。等

(topページに必要なコンテンツ)
・病院からのお知らせ
・はじめてご来院の方へ
-外来受診のご案内
-診療担当・日時
-休診・代診のお知らせ
-入院のご案内
-セカンドオピニオンについて
・お見舞いの皆様へ
・診療科・施設のご案内
-※別途、診療科・施設については添付ファイルを参照ください。
・当院の紹介
・採用情報
・先進医療センター
・周産期医療センター
・消化器病センター
・乳腺診療センター
・地域医療連携への取り組み
ブルーを基調(ロゴカラーコード:24569d)差し色はお任せ
デザインの作成は、Photoshop・Fireworksのみとなります。Illustratorでの作成は不可とします。
(デザイン参考URL)
http://www.tomaru-kenseikai.gr.jp/
http://www.hanamizuki-kai.or.jp/
http://kobe.nskmu.ac.jp/

現サイトのURLにつきましては、個別にメッセージにてお送りさせて頂きますので、希望される方はメッセージをお送りください。
診療科・その他施設一覧ファイルを追加しました。
既存サイトのURLをお伝えした場合、既存サイトのデザインと同じようなご提案が多いため、期間を延長させて頂きます。
既存サイトのURLはお伝えしませんので、斬新なデザインのご提案をお待ちしております。

全体的にスッキリとしている。病院側の伝えたいポイントをしっかりと捉えている。見やすい等、選定理由となりました。

今回、デザイン作成に応募いただきましてありがとうございます。ご提案いただきました全てのデザインをクライアント様に確認いただき、選定させていただきました。
今後とも、機会がありましたら宜しくお願いいたします。

```html
<!DOCTYPE html>
<html lang="ja">
<head>
<meta charset="utf-8">
<title>キャッチフレーズ 総合病院</title>
<link href="https://fonts.googleapis.com/css2?family=Noto+Sans+JP:wght@400;700&display=swap" rel="stylesheet">
<style>
:root{
  --brand:#24569d;
  --brand-light:#e6eef9;
  --line:#9fb7dd;
  --bg:#dde6f2;
  --panel:#ffffff;
  --text:#333;
  --muted:#666;
  --pink:#f3c3d8;
  --pink-text:#d2477f;
  --accent:#e77a2b;
}
*{box-sizing:border-box;margin:0;padding:0}
html,body{width:1200px;height:2584px;overflow:hidden}
body{font-family:"Noto Sans JP",sans-serif;color:var(--text);background:var(--bg);font-size:15px;line-height:1.45;position:relative}
.site-header{height:120px;background:linear-gradient(#fff,#eef3fa);position:relative}
.brand{position:absolute;left:24px;top:18px;display:flex;align-items:center;gap:14px}
.brand-mark{width:70px;height:70px;background:var(--brand)}
.brand-name{color:var(--brand);font-size:34px;line-height:1.1}
.brand-name small{display:block;font-size:24px}
.contact{position:absolute;right:28px;top:10px;text-align:right;color:var(--brand)}
.tel{font-size:30px;font-weight:700;display:flex;align-items:center;gap:8px;justify-content:flex-end}
.hours{font-size:15px}
.util{font-size:14px;margin-top:6px;display:flex;gap:18px;justify-content:flex-end}
.util span::before{content:"▸";margin-right:4px}
.global-nav{height:32px;background:linear-gradient(#3d72bd,var(--brand));display:flex;padding-left:24px}
.global-nav a{color:#fff;text-decoration:none;font-size:18px;padding:3px 18px;border-right:1px solid #6f95cf}
.side{position:absolute;left:24px;top:168px;width:296px}
.side-box{background:var(--panel);border:1px solid var(--line)}
.side-head{background:var(--brand-light);color:var(--brand);font-weight:700;padding:4px 12px;border-bottom:1px solid var(--line);font-size:16px}
.side-head.sub{color:var(--accent);background:#fff;border-top:1px solid var(--line)}
.side-list{list-style:none;padding:4px 16px}
.side-list li{font-size:15px;padding:5px 0;border-bottom:1px dotted #c5d3ea}
.side-list li::before{content:"●";color:var(--brand);font-size:10px;margin-right:8px;vertical-align:2px}
.banner{margin-top:24px;height:70px;background:var(--pink);border:3px solid #fff;outline:1px solid #e6a0bf;display:flex;align-items:center;justify-content:center;color:var(--pink-text);font-size:24px;font-weight:700}
.main{position:absolute;left:336px;top:168px;width:840px}
.hero{height:272px;background:linear-gradient(100deg,#cfe1f3,#f4f8fc 55%,#bcd3ea);position:relative}
.hero p{position:absolute;left:250px;top:14px;color:#fff;font-size:32px;font-weight:700;line-height:1.4;background:rgba(36,86,157,.55);padding:4px 18px}
.panel{background:var(--panel);border:1px solid var(--line);margin-top:16px}
.panel-head{background:var(--brand-light);color:var(--brand);font-weight:700;font-size:18px;padding:5px 14px;border-bottom:1px solid var(--line)}
.news{list-style:none;padding:8px 18px 0}
.news li{font-size:15px;padding:5px 0;border-bottom:1px dotted #c5d3ea}
.news time{color:var(--brand);margin-right:14px}
.more{text-align:right;font-size:14px;color:var(--brand);padding:6px 18px 10px}
.guide{padding:12px 18px 18px}
.guide h3{color:var(--brand);font-size:17px;margin-top:12px}
.guide h3:first-child{margin-top:0}
.guide h3::before{content:"▍";color:var(--brand)}
.guide p{font-size:15px;padding-left:18px;color:var(--muted);line-height:1.65}
.facilities{display:grid;grid-template-columns:1fr 1fr;padding:16px 24px;gap:4px 30px}
.facilities span{font-size:15px}
.facilities span::before{content:"●";color:var(--brand);font-size:10px;margin-right:8px;vertical-align:2px}
.centers{display:grid;grid-template-columns:1fr 1fr;gap:22px;margin-top:34px}
.center{background:var(--panel);border:1px solid var(--line);height:340px}
.center-body{display:flex;gap:14px;padding:14px}
.center-photo{width:176px;height:140px;flex:none;background:linear-gradient(135deg,#eef2f6,#c7d3df)}
.center-body p{font-size:14px;color:var(--muted);line-height:1.5}
.community{margin-top:34px}
.community p{padding:14px 24px;font-size:14px;color:var(--muted);line-height:1.6}
.site-footer{position:absolute;left:0;bottom:0;width:1200px;height:48px;background:var(--brand);color:#fff;font-size:14px;text-align:right;padding:14px 28px}
</style>
</head>
<body>
<header class="site-header">
  <div class="brand"><span class="brand-mark"></span><div class="brand-name">キャッチフレーズ<small>キャッチフレーズキャッチ</small></div></div>
  <div class="contact">
    <div class="tel"><svg width="28" height="26" viewBox="0 0 28 26"><path d="M4 8c0-4 20-4 20 0l-4 3-3-3h-6l-3 3z M6 12h16l2 12H4z" fill="#24569d"/></svg>03-9876-5432</div>
    <div class="hours">平日9:00～17:00</div>
    <div class="util"><span>はじめてご来院の方へ</span><span>交通案内</span></div>
  </div>
</header>
<nav class="global-nav">
  <a>ホーム</a><a>診療科のご案内</a><a>当院のご紹介</a><a>施設のご案内</a><a>お見舞いの皆様へ</a><a>交通アクセス</a>
</nav>

<aside class="side">
  <div class="side-box">
    <div class="side-head">診療科のご案内</div>
    <div class="side-head sub">内科</div>
    <ul class="side-list"><li>総合内科・漢方内科</li><li>神経内科</li><li>消化器科</li><li>循環器内科</li><li>呼吸器内科</li><li>腎臓内科</li><li>糖尿病内科</li></ul>
    <div class="side-head sub">外科</div>
    <ul class="side-list"><li>内視鏡外科</li><li>乳腺外科</li><li>脳神経外科</li><li>心臓血管外科</li><li>整形外科</li><li>皮膚科</li><li>泌尿器科</li><li>耳鼻咽喉科</li><li>眼科</li><li>歯科</li></ul>
    <div class="side-head sub">診療科</div>
    <ul class="side-list"><li>放射線診断科</li><li>リハビリテーション科</li><li>麻酔科</li><li>病理科</li></ul>
  </div>
  <div class="banner">お見舞いの方へ</div>
  <div class="banner">採用情報</div>
</aside>

<main class="main">
  <div class="hero" role="img" aria-label="病院の建物と医療スタッフの写真">
    <p>救急患者の受入れを断らず<br>地域に最先端医療で貢献します</p>
  </div>

  <section class="panel">
    <h2 class="panel-head">お知らせ</h2>
    <ul class="news">
      <li><time>2013.03.04</time>Lorem ipsum dolor sit amet, consectetur adipisicing elit,</li>
      <li><time>2013.03.08</time>Lorem ipsum dolor sit amet, consectetur adipisicing elit,</li>
      <li><time>2013.03.12</time>Lorem ipsum dolor sit amet, consectetur adipisicing elit, sed do eiusmod tempor incididunt ut labore</li>
      <li><time>2013.03.14</time>Lorem ipsum dolor sit amet, consectetur adipisicing elit,</li>
      <li><time>2013.03.18</time>Lorem ipsum dolor sit amet, consectetur adipisicing elit,</li>
    </ul>
    <div class="more">▸もっと詳しく</div>
  </section>

  <section class="panel">
    <h2 class="panel-head">はじめてご来院の方へ</h2>
    <div class="guide">
      <h3>外来受診のご案内</h3><p>Lorem ipsum dolor sit amet, consectetur adipisicing elit, sed do eiusmod tempor incididunt ut labore et dolore magna aliqua. Ut enim ad minim veniam.</p>
      <h3>診療担当・日時</h3><p>Lorem ipsum dolor sit amet, consectetur adipisicing elit, sed do eiusmod tempor incididunt ut labore et dolore magna aliqua. Ut enim ad minim veniam, quis nostrud exercitation ullamco laboris nisi ut aliquip ex ea commodo consequat. Duis aute irure dolor in reprehenderit in voluptate velit esse cillum dolore eu fugiat nulla pariatur.</p>
      <h3>休診・代診のお知らせ</h3><p>Lorem ipsum dolor sit amet, consectetur adipisicing elit, sed do eiusmod tempor incididunt ut labore et dolore magna aliqua.</p>
      <h3>入院のご案内</h3><p>Lorem ipsum dolor sit amet, consectetur adipisicing elit, sed do eiusmod tempor incididunt ut labore et dolore magna aliqua. Ut enim ad minim veniam, quis nostrud exercitation.</p>
      <h3>セカンドオピニオンについて</h3><p>Lorem ipsum dolor sit amet, consectetur adipisicing elit, sed do eiusmod tempor incididunt ut labore et dolore magna aliqua.</p>
    </div>
  </section>

  <section class="panel" style="margin-top:34px">
    <h2 class="panel-head">治療・検査施設</h2>
    <div class="facilities">
      <span>通院リハビリテーションセンター</span><span>総合リハビリテーションセンター</span>
      <span>地域リハビリテーション広域支援センター</span><span>乳腺診療センター</span>
      <span>血液浄化センター</span><span>先進医療センター</span>
      <span>健診センター</span><span>透析室</span>
      <span>栄養管理課</span><span>薬局</span>
      <span>消化器病センター</span><span>臨床検査室</span>
      <span>周産期センター</span><span>MRI室・画像診断部</span>
    </div>
  </section>

  <div class="centers">
    <section class="center"><h2 class="panel-head">先進医療センター</h2><div class="center-body"><div class="center-photo" role="img" aria-label="医療機器の写真"></div><p>Lorem ipsum dolor sit amet, consectetur adipisicing elit, sed do eiusmod tempor incididunt ut labore et dolore magna aliqua. Ut enim ad minim veniam, quis nostrud exercitation ullamco laboris nisi ut aliquip ex ea commodo consequat. Duis aute irure dolor in reprehenderit in voluptate velit esse cillum dolore eu fugiat nulla pariatur.</p></div></section>
    <section class="center"><h2 class="panel-head">周産期医療センター</h2><div class="center-body"><div class="center-photo" role="img" aria-label="周産期医療の写真"></div><p>Lorem ipsum dolor sit amet, consectetur adipisicing elit, sed do eiusmod tempor incididunt ut labore et dolore magna aliqua. Ut enim ad minim veniam, quis nostrud exercitation ullamco laboris nisi ut aliquip ex ea commodo consequat. Duis aute irure dolor in reprehenderit in voluptate velit esse cillum dolore eu fugiat nulla pariatur.</p></div></section>
    <section class="center"><h2 class="panel-head">消化器病センター</h2><div class="center-body"><div class="center-photo" role="img" aria-label="診察風景の写真"></div><p>Lorem ipsum dolor sit amet, consectetur adipisicing elit, sed do eiusmod tempor incididunt ut labore et dolore magna aliqua. Ut enim ad minim veniam, quis nostrud exercitation ullamco laboris nisi ut aliquip ex ea commodo consequat. Duis aute irure dolor in reprehenderit in voluptate velit esse cillum dolore eu fugiat nulla pariatur.</p></div></section>
    <section class="center"><h2 class="panel-head">乳腺診療センター</h2><div class="center-body"><div class="center-photo" role="img" aria-label="検査室の写真"></div><p>Lorem ipsum dolor sit amet, consectetur adipisicing elit, sed do eiusmod tempor incididunt ut labore et dolore magna aliqua. Ut enim ad minim veniam, quis nostrud exercitation ullamco laboris nisi ut aliquip ex ea commodo consequat. Duis aute irure dolor in reprehenderit in voluptate velit esse cillum dolore eu fugiat nulla pariatur.</p></div></section>
  </div>

  <section class="panel community">
    <h2 class="panel-head">地域医療連携への取り組み</h2>
    <p>Lorem ipsum dolor sit amet, consectetur adipisicing elit, sed do eiusmod tempor incididunt ut labore et dolore magna aliqua. Ut enim ad minim veniam, quis nostrud exercitation ullamco laboris nisi ut aliquip ex ea commodo consequat. Duis aute irure dolor in reprehenderit in voluptate velit esse cillum dolore eu fugiat nulla pariatur. Excepteur sint occaecat cupidatat non proident, sunt in culpa qui officia deserunt mollit anim id est laborum. Sed ut perspiciatis unde omnis iste natus error sit voluptatem accusantium doloremque laudantium.</p>
  </section>
</main>

<footer class="site-footer">Copyright (C) ○○病院 All Rights Reserved.</footer>
</body>
</html>
```